Business Card Design for Occupational Medicine Start Up Company

We need to design a professional business card. We are a healthcare company providing occupational medicine services to blue collar industries. We are professional, efficient and high quality service providers.

Target Market(s)

Blue Collar Industry: Shipbuilding, Ports, Trucking Companies; The Executives and Safety Officers for these companies

Industry/Entity Type

Healthcare

Contact Information for Business Card

Logo, Name, Title, Email, Phone

Other font styles liked:
• Please match our Brand Guide

Requirements
Must have
• Our Company Colors and Logo

```html
<!DOCTYPE html>
<html lang="en">
<head>
<meta charset="utf-8">
<title>Crewline Clinics – Business Card</title>
<link href="https://fonts.googleapis.com/css2?family=Montserrat:wght@400;500;600;700&display=swap" rel="stylesheet">
<style>
  :root {
    --navy: #2a3580;
    --white: #ffffff;
    --gray-text: #6d6e71;
    --amber: #f5a94a;
    --backdrop: #e6e6e6;
  }
  html, body {
    margin: 0;
    padding: 0;
    width: 1200px;
    height: 900px;
    overflow: hidden;
    background: var(--backdrop);
    font-family: "Montserrat", sans-serif;
  }
  .card {
    position: absolute;
    left: 328px;
    width: 445px;
    height: 254px;
    box-sizing: border-box;
  }
  .card-front {
    top: 165px;
    background: var(--white);
  }
  .card-back {
    top: 467px;
    background: var(--navy);
  }
  .brand-panel {
    position: absolute;
    left: 0;
    top: 0;
    width: 171px;
    height: 100%;
    background: var(--navy);
  }
  .brand-panel-tab {
    position: absolute;
    left: 171px;
    top: 49px;
    width: 2px;
    height: 156px;
    background: var(--navy);
    border-radius: 0 1px 1px 0;
  }
  .brand-mark {
    position: absolute;
    left: 0;
    right: 0;
    display: flex;
    flex-direction: column;
    align-items: center;
    gap: 10px;
  }
  .brand-panel .brand-mark { top: 96px; }
  .card-back .brand-mark { top: 80px; }
  .brand-dot {
    border-radius: 50%;
    background: var(--amber);
  }
  .brand-panel .brand-dot { width: 30px; height: 30px; }
  .card-back .brand-dot { width: 34px; height: 34px; }
  .brand-name {
    color: var(--white);
    font-weight: 600;
    letter-spacing: 0.06em;
    text-transform: uppercase;
    white-space: nowrap;
  }
  .brand-panel .brand-name { font-size: 15px; }
  .card-back .brand-name { font-size: 22px; }
  .contact {
    position: absolute;
    left: 192px;
    top: 83px;
  }
  .person-name {
    margin: 0;
    font-size: 15px;
    color: var(--navy);
    font-weight: 400;
    letter-spacing: 0.02em;
    line-height: 1.2;
  }
  .person-name .first { font-weight: 700; }
  .person-title {
    margin: 2px 0 0;
    font-size: 14px;
    color: var(--gray-text);
    letter-spacing: 0.02em;
  }
  .contact-line {
    margin: 0;
    font-size: 12.5px;
    color: var(--gray-text);
    letter-spacing: 0.01em;
  }
  .contact-email { margin-top: 21px; margin-left: -2px; }
  .contact-phone { margin-top: 8px; margin-left: -2px; }
</style>
</head>
<body>
  <section class="card card-front">
    <div class="brand-panel">
      <div class="brand-mark">
        <span class="brand-dot"></span>
        <span class="brand-name">Crewline</span>
      </div>
    </div>
    <div class="brand-panel-tab"></div>
    <div class="contact">
      <p class="person-name"><span class="first">DANIEL</span> PLACEHOLDER</p>
      <p class="person-title">Cardiac Sonographer</p>
      <p class="contact-line contact-email">daniel.placeholder@crewlineclinics.com</p>
      <p class="contact-line contact-phone">555-014-2390</p>
    </div>
  </section>

  <section class="card card-back">
    <div class="brand-mark">
      <span class="brand-dot"></span>
      <span class="brand-name">Crewline Clinics</span>
    </div>
  </section>
</body>
</html>
```